Retro game shop business card design

We need a card designed both front and back. we already have a logo. The business name is called Brisk Copper Atlas and we work on customizing and modifying old velmora zuma tabs. Our website is briskcopperatlas.com

our business cards are often shown in glintly posts ans should be designed so that you can easy identify and see in am image. @briskcopperatlas.

Target Market(s)

men 13-40

Contact Information for Business Card

should have logo, wesbite, and if possible some artwork related to zuma tab mods

Font styles to use
Sans Serif

Colors

Designer to choose colors to be used in the design.

Requirements
Must have
• logo, website url www.briskcopperatlas.com, hastag #zumatabmods, email, support@briskcopperatlas.com. zuma tab imagry only (illustration preffered)
Nice to have
• illustrations, graphic design with zuma tab mods (see glintly #zumatabmods)
Should not have
• childlike depictions of zumatabs, kids, anything unrelated to zuma tab mods, no hands, no bertil, no pixel art

```html
<!DOCTYPE html>
<html lang="en">
<head>
<meta charset="utf-8">
<title>Brisk Copper Atlas – Business Card</title>
<link href="https://fonts.googleapis.com/css2?family=Work+Sans:wght@400;500;800&display=swap" rel="stylesheet">
<style>
  :root {
    --page-bg: #222222;
    --card-light: #ffffff;
    --card-dark: #3d3d3d;
    --ink: #1c1c1c;
    --ink-soft: #2a2a2a;
    --paper-text: #f4f4f4;
    --device-top: #d4d4d4;
    --device-mid: #bdbdbd;
    --device-low: #9c9c9c;
    --device-edge: #f2f2f2;
  }
  * { box-sizing: border-box; margin: 0; padding: 0; }
  html, body { width: 1200px; height: 900px; overflow: hidden; }
  body {
    background: var(--page-bg);
    font-family: "Work Sans", Arial, sans-serif;
    position: relative;
  }
  .card {
    position: absolute;
    top: 147px;
    width: 347px;
    height: 607px;
  }
  .card--front { left: 197px; background: var(--card-light); color: var(--ink); }
  .card--back { left: 657px; background: var(--card-dark); color: var(--paper-text); }

  .wordmark {
    font-weight: 800;
    text-transform: uppercase;
    font-size: 37px;
    line-height: 1.2;
    letter-spacing: 0;
    text-align: center;
    white-space: nowrap;
  }
  .card--front .wordmark {
    position: absolute;
    left: 33px;
    top: 44px;
    width: 282px;
    color: var(--ink);
  }
  .card--back .wordmark {
    position: absolute;
    left: 0;
    right: 0;
    top: 460px;
    color: var(--paper-text);
  }

  .contact {
    position: absolute;
    left: 33px;
    top: 380px;
    color: var(--ink-soft);
  }
  .contact__name {
    font-size: 26px;
    font-weight: 500;
    letter-spacing: 1px;
    line-height: 1;
    text-transform: uppercase;
    color: var(--ink);
  }
  .contact__role { font-size: 14px; margin-top: 6px; letter-spacing: 0.4px; }
  .contact__rule {
    width: 56px; height: 1px; background: var(--ink);
    margin: 11px 0 12px;
  }
  .contact__address, .contact__lines {
    font-size: 14px; line-height: 21px; letter-spacing: 0.4px;
  }
  .contact__lines { margin-top: 10px; }
  .contact__lines div { display: flex; }
  .contact__label { width: 48px; }

  .device-art {
    position: absolute;
    left: 89px;
    top: 47px;
    width: 168px;
    height: 279px;
    border: 3px solid var(--device-edge);
    border-radius: 5px 5px 36px 5px;
    background: linear-gradient(170deg, var(--device-top) 0%, var(--device-mid) 55%, var(--device-low) 100%);
    box-shadow: 0 6px 14px rgba(0, 0, 0, 0.28);
  }
  .hashtag {
    position: absolute;
    left: 0; right: 0;
    top: 344px;
    text-align: center;
    font-size: 21px;
    letter-spacing: 0.6px;
  }
</style>
</head>
<body>
  <section class="card card--front">
    <div class="wordmark">Brisk Copper<br>Atlas</div>
    <div class="contact">
      <div class="contact__name">Dorian Vale</div>
      <div class="contact__role">Director</div>
      <div class="contact__rule"></div>
      <div class="contact__address">482 N Larkspur Road<br>Fenwick, MN. 55123-4410</div>
      <div class="contact__lines">
        <div><span class="contact__label">Phone</span><span>: 800-555-0192</span></div>
        <div><span class="contact__label">Email</span><span>: support@briskcopperatlas.com</span></div>
        <div><span class="contact__label">Web</span><span>: www.briskcopperatlas.com</span></div>
      </div>
    </div>
  </section>

  <section class="card card--back">
    <div class="device-art" role="img" aria-label="Flat-style illustration of a grey retro handheld zuma tab console with screen, directional pad and two magenta buttons"></div>
    <div class="hashtag">#zumatabmods</div>
    <div class="wordmark">Brisk Copper<br>Atlas</div>
  </section>
</body>
</html>
```